Business Card Design for TrailStocked

TrailStocked is an online e-commerce store specializing in Outdoors Gear such as camping equipment, hunting and shooting equipment, tactical gear and more. See complete line at trailstocked.org
Logo: http://www.trailstocked.org/media/ID/Stocked.jpg
http://www.trailstocked.org/media/ID/TrailStocked-blue.jpg

Target Market(s)

20-40 Male

Industry/Entity Type

E-Commerce

```html
<!DOCTYPE html>
<html lang="en">
<head>
<meta charset="utf-8">
<title>TrailStocked Business Cards</title>
<link rel="stylesheet" href="https://fonts.googleapis.com/css2?family=Open+Sans:wght@700;800&family=Arimo:wght@400&display=swap">
<style>
  :root {
    --navy: #0c2a86;
    --white: #ffffff;
    --ice: #aab9de;
    --contact: #e4e8f3;
    --page: #ffffff;
  }
  * { margin: 0; padding: 0; box-sizing: border-box; }
  html, body {
    width: 1200px;
    height: 767px;
    overflow: hidden;
    background: var(--page);
  }
  .sheet {
    position: relative;
    width: 1200px;
    height: 767px;
  }
  .card {
    position: absolute;
    width: 550px;
    height: 313px;
    background: var(--navy);
    overflow: hidden;
    color: var(--white);
  }
  .card--front-centered { left: 38px; top: 38px; }
  .card--back-left      { left: 613px; top: 38px; }
  .card--front-corner   { left: 38px; top: 409px; }
  .card--back-right     { left: 617px; top: 409px; }

  .wordmark {
    position: absolute;
    font-family: "Open Sans", sans-serif;
    font-weight: 800;
    line-height: 1;
    letter-spacing: -0.01em;
    white-space: nowrap;
  }
  .tagline {
    position: absolute;
    font-family: "Open Sans", sans-serif;
    font-weight: 700;
    line-height: 1;
    white-space: nowrap;
  }
  .brand-ring {
    position: absolute;
    border: 5px solid var(--white);
    border-radius: 50%;
  }
  .backdrop-disc {
    position: absolute;
    border-radius: 50%;
    background: var(--ice);
    opacity: 0.9;
  }
  .contact {
    position: absolute;
    list-style: none;
    font-family: "Arimo", sans-serif;
    font-size: 15px;
    line-height: 20.6px;
    color: var(--contact);
  }

  /* Front, centred lockup */
  .card--front-centered .brand-ring { left: 211px; top: 26px; width: 128px; height: 128px; }
  .card--front-centered .wordmark { left: 0; width: 550px; text-align: center; top: 197px; font-size: 50px; }
  .card--front-centered .tagline { left: 0; width: 550px; text-align: center; top: 255px; font-size: 23.5px; }

  /* Back, details on left */
  .card--back-left .wordmark { left: 10px; top: 17px; font-size: 31px; }
  .card--back-left .tagline { left: 10px; top: 56px; font-size: 15px; }
  .card--back-left .contact { left: 10px; top: 136px; }
  .card--back-left .backdrop-disc { left: 250px; top: 26px; width: 284px; height: 284px; }

  /* Front, corner lockup */
  .card--front-corner .brand-ring { left: 15px; top: 209px; width: 83px; height: 83px; border-width: 4px; }
  .card--front-corner .wordmark { left: 108px; top: 216px; font-size: 48px; }
  .card--front-corner .tagline { left: 112px; top: 270px; font-size: 23px; }

  /* Back, details on right */
  .card--back-right .backdrop-disc { left: -20px; top: -10px; width: 270px; height: 270px; }
  .card--back-right .contact { left: 282px; top: 46px; }
  .card--back-right .wordmark { left: 250px; top: 244px; font-size: 32px; }
  .card--back-right .tagline { left: 252px; top: 280px; font-size: 15.5px; }
</style>
</head>
<body>
<main class="sheet">

  <section class="card card--front-centered" aria-label="Card front, centred lockup">
    <span class="brand-ring" aria-hidden="true"></span>
    <h1 class="wordmark">TrailStocked.com</h1>
    <p class="tagline">Outfitted for Camp, Hunt and Trail</p>
  </section>

  <section class="card card--back-left" aria-label="Card back, contact details left">
    <h2 class="wordmark">TrailStocked.com</h2>
    <p class="tagline">Outfitted for Camp, Hunt and Trail</p>
    <ul class="contact">
      <li>Dmitri Volkov</li>
      <li>Cell: 847 555 0142</li>
      <li>Office: 847 555 0178</li>
      <li>Purchasing Manager</li>
      <li>www.trailstocked.org</li>
      <li>PO BOX 286</li>
      <li>Ashbrook, IL 60412</li>
      <li>Purchasing@trailstocked.org</li>
    </ul>
    <span class="backdrop-disc" aria-hidden="true"></span>
  </section>

  <section class="card card--front-corner" aria-label="Card front, corner lockup">
    <span class="brand-ring" aria-hidden="true"></span>
    <h2 class="wordmark">TrailStocked.com</h2>
    <p class="tagline">Outfitted for Camp, Hunt and Trail</p>
  </section>

  <section class="card card--back-right" aria-label="Card back, contact details right">
    <span class="backdrop-disc" aria-hidden="true"></span>
    <ul class="contact">
      <li>Dmitri Volkov</li>
      <li>Cell: 847 555 0142</li>
      <li>Office: 847 555 0178</li>
      <li>Purchasing Manager</li>
      <li>www.trailstocked.org</li>
      <li>PO BOX 286</li>
      <li>Ashbrook, IL 60412</li>
      <li>Purchasing@trailstocked.org</li>
    </ul>
    <h2 class="wordmark">TrailStocked.com</h2>
    <p class="tagline">Outfitted for Camp, Hunt and Trail</p>
  </section>

</main>
</body>
</html>
```